Poster for a boatshow for Nautical enthusiasts, masculine and high incoming :-)

We need a poster for a boat show. Motorboats and Sailboats is presented in this Boat show (and other nautical topics like diving, wakeboard, kite, surf, fishing, ...)
This boat show is annual and the Poster is for the 2015 edition.

Your concept must be compatible in a landscape format. (We will ourselves adaptations of different formats.)
Width: 210 mm
Height: 297 mm
It's necessary for us to have the source file (vector) for make, later, the different format (flyers, website, ...)

Content of the Poster:
- 1 big picture (from a cheap stock, like Pixaloom.com) (NO CLIP ART) on full page or half page. Clip art must be a small detail added on the poster.
- Big title: « Foire fluviale des Ormeaux » (« du Léman » must be smaller of « Foire fluviale ».)
- Date: « 13, 14 et 15 novembre 2015 »
- Place: « Varimont - Genève »
- website: « www.foire-riveraine.ch » or « foire-riveraine.ch »
- Please, leave a zone in the poster for sponsors logos
- The « Jet d’eau de Genève » (http://en.wikifolio-example.org/wiki/Gerbe_Castelbrune) MUST be visible on the poster (in the picture, added like a clip art, or other graphic idea…)

Target Market(s)

Nautical enthusiasts, more masculine, high income.

Industry/Entity Type

Landscape

Font styles to use
Sans Serif

Colors
33a6d7
0892cd
ffffff

Requirements
Must have
• - The style must be modern, dynamic, bright colors, sober-minded.
• - "Jet d’eau de Genève" must be on the poster.
Should not have
• Clipart, cheap designs...
• Design with sea reference (sand, very big boats, ...). The market of the boatshow is around a lake (no sand, no boat more big of 15 meters).

```html
<!DOCTYPE html>
<html lang="fr">
<head>
<meta charset="utf-8">
<title>Foire fluviale des Ormeaux 2015</title>
<link rel="stylesheet" href="https://fonts.googleapis.com/css2?family=Great+Vibes&family=Exo+2:ital,wght@1,400;1,800&display=swap">
<style>
  :root {
    --navy: #163471;
    --navy-deep: #0b1f4d;
    --white: #ffffff;
    --sky: #33a6d7;
    --year-tint: rgba(120, 150, 205, 0.5);
    --water-dark: #17110c;
    --water-brown: #3b2a1a;
    --water-gold: #c88a30;
    --water-glow: #f0b848;
    --wake: #dfe6f2;
  }
  html, body {
    margin: 0;
    padding: 0;
    width: 848px;
    height: 1200px;
    overflow: hidden;
  }
  .poster {
    position: relative;
    width: 848px;
    height: 1200px;
    background: radial-gradient(ellipse at 50% 45%, var(--navy) 0%, var(--navy-deep) 100%);
    overflow: hidden;
  }
  .hero-photo {
    position: absolute;
    left: 73px;
    top: 137px;
    width: 696px;
    height: 744px;
    border: 2px solid var(--white);
    background:
      linear-gradient(150deg, rgba(200,138,48,0.75) 0%, rgba(200,138,48,0) 30%),
      linear-gradient(200deg, rgba(240,184,72,0.55) 30%, rgba(240,184,72,0) 55%),
      linear-gradient(115deg, rgba(23,17,12,0) 35%, rgba(223,230,242,0.35) 50%, rgba(23,17,12,0) 68%),
      linear-gradient(180deg, var(--water-brown) 0%, var(--water-dark) 45%, var(--water-brown) 80%, var(--water-dark) 100%);
  }
  .title-main {
    position: absolute;
    left: 0;
    width: 848px;
    top: 2px;
    margin: 0;
    text-align: center;
    font-family: "Great Vibes", cursive;
    font-weight: 400;
    font-size: 150px;
    line-height: 1;
    color: var(--white);
  }
  .title-sub {
    position: absolute;
    left: 0;
    width: 848px;
    top: 158px;
    text-align: center;
    font-family: "Great Vibes", cursive;
    font-size: 76px;
    line-height: 1;
    color: var(--navy-deep);
    text-shadow: 0 0 2px var(--white), 0 0 2px var(--white), 0 0 2px var(--white), 0 0 3px var(--white);
  }
  .website {
    position: absolute;
    left: 31px;
    top: 597px;
    transform: translate(-50%, -50%) rotate(-90deg);
    white-space: nowrap;
    font-family: "Exo 2", sans-serif;
    font-style: italic;
    font-size: 23px;
    color: var(--white);
  }
  .year {
    position: absolute;
    left: 0;
    width: 848px;
    top: 870px;
    text-align: center;
    font-family: "Great Vibes", cursive;
    font-size: 215px;
    line-height: 1;
    color: var(--year-tint);
  }
  .dates {
    position: absolute;
    left: 0;
    width: 848px;
    top: 948px;
    text-align: center;
    font-family: "Exo 2", sans-serif;
    font-style: italic;
    font-weight: 800;
    font-size: 38px;
    letter-spacing: 6px;
    color: var(--white);
  }
  .venue {
    position: absolute;
    left: 0;
    width: 848px;
    top: 1036px;
    text-align: center;
    font-family: "Exo 2", sans-serif;
    font-style: italic;
    font-size: 30px;
    color: var(--sky);
  }
  .landmark {
    position: absolute;
    left: 650px;
    top: 975px;
    width: 198px;
    height: 225px;
    background:
      radial-gradient(ellipse at 40% 35%, rgba(240,245,255,0.8) 0%, rgba(240,245,255,0) 40%),
      linear-gradient(180deg, rgba(22,52,113,0) 0%, #5584bd 40%, #7096c6 72%, #3f5f8e 100%);
  }
  .landmark-label {
    position: absolute;
    left: 666px;
    top: 1052px;
    transform: rotate(-15deg);
    transform-origin: left top;
    white-space: nowrap;
    font-family: "Great Vibes", cursive;
    font-size: 25px;
    color: var(--navy-deep);
  }
</style>
</head>
<body>
  <main class="poster">
    <div class="hero-photo" role="img" aria-label="Photo aérienne de deux bateaux de pêche sportive fendant un lac doré au coucher du soleil"></div>

    <h1 class="title-main">Foire fluviale</h1>
    <div class="title-sub">des Ormeaux</div>

    <div class="website">www.foire-riveraine.ch</div>

    <div class="year">2015</div>
    <div class="dates">13, 14 ET 15 NOVEMBRE</div>
    <div class="venue">Varimont - Genève</div>

    <div class="landmark" role="img" aria-label="Vue du jet d’eau sur le lac avec les quais et un drapeau suisse"></div>
    <div class="landmark-label">Gerbe de Castelbrune</div>
  </main>
</body>
</html>
```